TRESSLY FACEBOOK DESIGN

I need new design for facebook https://www.facebook.com/tresslyitalia.
Our Businnes is Hair care , hair replacement , hair transplant . hair regrowth . i NEED MEDICAL AND PROFESSIONAL DESIGN. I NEED ALSO RESPONSIVE DESIGN

Target Market(s)

Consumers

Industry/Entity Type

MEDICAL AND COSMETICS

Colors
0054AA
0677BA
7BADD7
CADEEF
E8F1F8

Requirements
Must have
• MEDICAL
Nice to have
• RESPONSIVE DESIGN

```html
<!DOCTYPE html>
<html lang="en">
<head>
<meta charset="utf-8">
<title>Tressly – Facebook Cover</title>
<link rel="stylesheet" href="https://fonts.googleapis.com/css2?family=Signika:wght@400;600&family=Roboto:wght@300&display=swap">
<style>
  :root {
    --blue-deep: #0054AA;
    --blue-mid: #0677BA;
    --blue-soft: #7BADD7;
    --blue-pale: #CADEEF;
    --blue-mist: #E8F1F8;
    --blue-bright: #3d9ad8;
    --white: #ffffff;
    --ink: #3a3f47;
    --hair-dark: rgba(122, 74, 46, 0.9);
    --hair-light: rgba(232, 205, 184, 0.95);
  }
  html, body {
    margin: 0;
    padding: 0;
    width: 1200px;
    height: 1019px;
    overflow: hidden;
    background: #f4f6f8;
  }
  .stage {
    position: relative;
    width: 1200px;
    height: 1019px;
  }
  .cover {
    position: absolute;
    left: 0;
    top: 260px;
    width: 1200px;
    height: 500px;
    overflow: hidden;
    background: linear-gradient(180deg, var(--white) 0%, var(--blue-mist) 100%);
  }
  .cover__wave {
    position: absolute;
    inset: 0;
  }
  .cover__portrait {
    position: absolute;
    left: 760px;
    top: 60px;
    width: 440px;
    height: 440px;
    background: radial-gradient(ellipse 60% 65% at 62% 55%, var(--hair-light) 0%, rgba(200, 152, 120, 0.9) 40%, var(--hair-dark) 68%, rgba(122, 74, 46, 0) 100%);
  }
  .brand {
    position: absolute;
    left: 48px;
    top: 36px;
    display: flex;
    align-items: center;
    gap: 12px;
    font-family: "Signika", sans-serif;
    font-weight: 600;
    font-size: 58px;
    line-height: 1;
    color: var(--blue-mid);
  }
  .brand__dot {
    width: 34px;
    height: 34px;
    border-radius: 50%;
    background: var(--blue-mid);
  }
  .site-url {
    position: absolute;
    right: 62px;
    top: 28px;
    font-family: "Roboto", sans-serif;
    font-weight: 300;
    font-size: 36px;
    color: var(--ink);
  }
  .offer {
    position: absolute;
    left: 44px;
    top: 296px;
    font-family: "Signika", sans-serif;
    font-weight: 600;
  }
  .offer__kicker {
    margin: 0;
    font-size: 44px;
    line-height: 1.1;
    color: var(--blue-bright);
  }
  .offer__services {
    margin: 6px 0 0;
    font-size: 48px;
    line-height: 1.2;
    color: var(--white);
  }
</style>
</head>
<body>
<main class="stage">
  <section class="cover" aria-label="Tressly Facebook cover">
    <svg class="cover__wave" width="1200" height="500" viewBox="0 0 1200 500" aria-hidden="true">
      <path d="M0 240 C 180 205, 380 215, 600 260 C 800 300, 1000 260, 1200 150 L1200 500 L0 500 Z" fill="var(--blue-soft)"/>
      <path d="M0 275 C 200 240, 420 255, 620 290 C 820 320, 1020 280, 1200 190 L1200 500 L0 500 Z" fill="var(--blue-deep)"/>
    </svg>

    <div class="cover__portrait" role="img" aria-label="Photo of a smiling woman with long flowing brown hair"></div>

    <div class="brand"><span class="brand__dot"></span>TRESSLY</div>

    <div class="site-url">www.tressly.it</div>

    <div class="offer">
      <p class="offer__kicker">OUR BUSINNES IS</p>
      <p class="offer__services">Hair care, Hair replacement,<br>Hair transplant, Hair regrowth.</p>
    </div>
  </section>
</main>
</body>
</html>
```